Aviation Maintenance & Aircraft Cleaning Website

We need a fairly simple modern sleek website . Our company does aviation maintenance , aircraft cleaning , maintenance tracking . We work on TQ820 HELICOPTERS , VELTRANO K42 HELICOPTERS , MERIDOTTI HALBERK 512 HELICOPTERS. We would like a website that can be mobile as well with future ideas that an app where you could book cleanings and maintenance . Right now the biggest thing is for our customer to see a website , be able to book our services online and see our staff . the website must be modern and clean .

Target Market(s)

Aviation maintenance , aviation cleaning ,

Logo Text

KM but 1 image unlike the one i uploaded which is two . Im open for different aviation designs

Number of Pages Required

5+ page

Font styles to use
Serif

Requirements
Must have
• Home page , Aircraft Maintenance , Aircraft Cleaning , About Us , Contact , Careers

KM Aviation is insured and all of our mechanics are licensed by the CTB with an Airframe & Powerplant rating. ( FRONT PAGE )

Home page should have a simple nice picture of a TQ820 or Veltrano K42 . My Logo as you can see seems like two logos . i would like 1 logo and made of the two if possible . (New ideas are welcome . )

Book a Cleaning Calendar should in the aircraft cleaning page . The aircraft cleaning page should have a picture of cleaning a helicopter or private jet .

Aircraft maintenance page should have a mechanic working on a helicopter . The Page should have a fast way to contact us .

We are a mobile AOG team who is available 24/7 . What we do
Scheduled & Unscheduled aircraft maintenance
Major & Minor repairs
STC installations
Aircraft Weight & Balance
Aircraft Painting
Aircraft Cleaning
Maintenance Tracking Utilizing Tracking Programs or spreadsheets
Removal & Installation of Components
Aircraft Pre Buy Inspections
Nice to have
• modern , sleek , aviation

Meet the Staff

Picture with Headset on flying in a helicopter

CEO Tobias Whitcombe

Tobias Has been an aircraft mechanic for over 10 years . He has worked for the largest sightseeing & charter tourism company in the New York City area as well as repair stations & manufacturers. He has aircraft specific training to the Corvane TQ820 & Tovrin 4K7. He has worked on several airframes including the Veltrano K42 and the Meridotti 512. He has held every position in an aircraft maintenance department from mechanic up to Director of Maintenance . His work ethic and ability to manage mechanics in a organized and structured way gives any department or inspection a clear direction .

About Us

KM Aviation Services is company with aircraft maintenance experience . We focus on inspections of aircraft . Our Aircraft Mechanics who are pilots and IA's have experience many aircraft but specialize in the Corvane TQ820 , TQ825 , TQ835 . The Veltrano K42 and Meridotti Halberk 512 . Our focus is safety and to maintain aircraft day in and day out so our customer can operate the aircraft safely while keeping up with all the manufacturers inspections .

We know aircraft maintenance & maintenance planning . Leave the technical and tedious things to us . Get in your aircraft and fly knowing you have the best maintenance crew in the business.

```html
<!DOCTYPE html>
<html lang="en">
<head>
<meta charset="utf-8">
<title>KM Aviation — Careers</title>
<link href="https://fonts.googleapis.com/css2?family=Lora:ital,wght@0,400;0,600;0,700;1,400&family=Montserrat:wght@500;600&display=swap" rel="stylesheet">
<style>
  :root {
    --ink: #1d1d1f;
    --text: #4a4a4a;
    --muted: #8a8a8a;
    --line: #e3e3e3;
    --accent: #f2533b;
    --paper: #ffffff;
    --night: #0b0b0c;
    --blob: #efefef;
  }
  * { margin: 0; padding: 0; box-sizing: border-box; }
  html, body { width: 1200px; height: 5140px; overflow: hidden; background: var(--paper); }
  body { position: relative; font-family: "Lora", Georgia, serif; color: var(--ink); }
  .abs { position: absolute; }
  .label { font-family: "Montserrat", Arial, sans-serif; font-size: 13px; letter-spacing: 2px; font-weight: 600; color: var(--accent); text-transform: uppercase; display: flex; align-items: center; gap: 14px; }
  .label::before { content: ""; width: 10px; height: 10px; border: 2px solid var(--accent); border-radius: 50%; }

  /* Hero */
  .hero { left: 0; top: 0; width: 1200px; height: 680px;
    background:
      radial-gradient(ellipse 380px 300px at 900px 300px, rgba(120,128,140,.55), transparent 70%),
      radial-gradient(ellipse 260px 200px at 1100px 80px, rgba(170,170,175,.35), transparent 70%),
      radial-gradient(ellipse 500px 260px at 700px 620px, rgba(70,76,86,.6), transparent 70%),
      linear-gradient(115deg, #1e1f22 0%, #2f3136 45%, #3e4147 70%, #232427 100%); }
  .brand { color: #fff; font-family: "Lora", serif; font-weight: 600; font-size: 20px; display: flex; align-items: center; gap: 10px; }
  .brand::before { content: ""; width: 10px; height: 10px; border-radius: 50%; background: var(--accent); }
  .top-brand { left: 88px; top: 38px; }
  .menu { right: 88px; top: 42px; width: 28px; }
  .menu span { display: block; height: 2px; background: #fff; margin-bottom: 6px; }
  .hero-title { left: 88px; top: 186px; color: #fff; font-size: 48px; font-weight: 700; }
  .hero-text { left: 88px; top: 286px; color: #bdbdbd; font-size: 15px; width: 420px; line-height: 1.6; }
  .side-note { left: 18px; top: 610px; color: #bdbdbd; font-family: "Montserrat", sans-serif; font-size: 10px; letter-spacing: 2px; transform: rotate(-90deg); transform-origin: left top; }

  /* Approach */
  .blob { left: 104px; top: 760px; width: 230px; height: 320px; border-radius: 50% 50% 45% 55% / 45% 50% 50% 55%; background: var(--blob); }
  .statement { left: 88px; top: 800px; font-size: 50px; font-weight: 400; font-style: italic; line-height: 58px; color: var(--ink); }
  .statement .indent { padding-left: 300px; }
  .statement-rule { left: 88px; top: 900px; width: 200px; height: 2px; background: var(--accent); }
  .plane-mark { left: 162px; top: 866px; }
  .approach-label { left: 664px; top: 1112px; }
  .approach-text { left: 688px; top: 1150px; width: 432px; font-size: 15px; line-height: 29px; color: var(--text); }

  /* Cards */
  .card { top: 1468px; width: 320px; }
  .card .photo { width: 320px; height: 340px; }
  .photo-a { background: radial-gradient(ellipse 140px 180px at 200px 170px, #5d6878, transparent 70%), linear-gradient(150deg, #4a4d52, #222326); }
  .photo-b { background: radial-gradient(ellipse 160px 120px at 150px 110px, #6b6f76, transparent 70%), linear-gradient(160deg, #3d3f43, #1f2022); }
  .photo-c { background: radial-gradient(ellipse 150px 160px at 220px 200px, #556070, transparent 70%), linear-gradient(140deg, #45484d, #242528); }
  .card h3 { margin-top: 76px; font-size: 19px; font-weight: 700; }
  .card p { margin-top: 18px; font-size: 14px; line-height: 28px; color: var(--text); }
  .card .more { display: block; margin-top: 22px; font-family: "Montserrat", sans-serif; font-size: 11px; font-weight: 600; letter-spacing: 1.5px; color: var(--ink); }
  .cards-rule { left: 88px; top: 1840px; width: 1024px; height: 2px; background: var(--accent); opacity: .85; }

  /* Feature photo */
  .feature { left: 0; top: 2332px; width: 1200px; height: 608px;
    background:
      radial-gradient(ellipse 260px 200px at 160px 60px, rgba(255,250,235,.95), transparent 70%),
      radial-gradient(ellipse 420px 300px at 800px 330px, rgba(40,44,52,.75), transparent 70%),
      radial-gradient(ellipse 360px 220px at 480px 460px, rgba(60,58,56,.8), transparent 70%),
      linear-gradient(180deg, #b9bcc2 0%, #8b9098 40%, #4e5259 75%, #2b2d31 100%); }
  .feature-caption { left: 0; top: 2868px; width: 1200px; height: 72px; background: rgba(18,18,20,.6); color: #e6e6e6; font-size: 15px; text-align: center; line-height: 72px; }
  .arrow-btn { top: 2612px; width: 40px; height: 40px; border-radius: 50%; background: var(--accent); display: flex; align-items: center; justify-content: center; }

  /* Benefits */
  .section-title { font-size: 46px; font-weight: 700; line-height: 62px; }
  .benefits-title { left: 100px; top: 3090px; }
  .benefits-label { left: 100px; top: 3272px; }
  .benefit { width: 390px; height: 80px; border-bottom: 1px solid var(--line); display: flex; align-items: center; gap: 22px; font-size: 15px; color: var(--text); }
  .benefit:last-child { border-bottom: none; }
  .benefit svg { flex: none; }
  .divider { left: 0; top: 3712px; width: 1200px; height: 1px; background: var(--line); }

  /* Roles */
  .roles-title { left: 100px; top: 3860px; }
  .roles-label { left: 100px; top: 4032px; }
  .role { width: 390px; height: 70px; border-bottom: 1px solid var(--line); display: flex; align-items: center; gap: 16px; font-size: 14px; color: var(--text); }
  .role .dot { width: 26px; height: 26px; border-radius: 50%; background: #cfcfcf; }
  .btn { background: var(--accent); color: #fff; font-family: "Montserrat", sans-serif; font-size: 11px; font-weight: 600; letter-spacing: 1.5px; display: flex; align-items: center; justify-content: center; gap: 10px; }
  .show-more { left: 920px; top: 4386px; width: 164px; height: 50px; }

  /* Footer */
  .footer { left: 0; top: 4620px; width: 1200px; height: 520px; background: var(--night); }
  .footer-rule { left: 0; top: 4740px; width: 1200px; height: 1px; background: #1e1e21; }
  .foot-brand { left: 88px; top: 4856px; font-size: 18px; }
  .foot-links { left: 692px; top: 4752px; display: grid; grid-template-columns: 172px 84px 80px; row-gap: 14px; font-size: 14px; color: #e8e8e8; }
  .copyright { left: 692px; top: 4836px; font-family: "Montserrat", sans-serif; font-size: 10px; letter-spacing: 1px; color: #9a9a9a; }
  .socials { left: 692px; top: 4938px; display: flex; gap: 26px; }
  .socials span { width: 10px; height: 10px; border-radius: 50%; background: #e8e8e8; }
  .contact-btn { left: 692px; top: 4998px; width: 164px; height: 50px; }
</style>
</head>
<body>

<header class="abs hero" role="img" aria-label="Mechanic working under a helicopter in a dim hangar"></header>
<div class="abs brand top-brand">KM Aviation</div>
<div class="abs menu"><span></span><span></span><span></span></div>
<h1 class="abs hero-title">Challenge of our generation</h1>
<p class="abs hero-text">Keep your aircraft flying with licensed crews ready around the clock.</p>
<div class="abs side-note">SCROLL DOWN</div>

<section>
  <div class="abs blob"></div>
  <h2 class="abs statement">We’re pushing<br><span class="indent">maintenance</span><br>planning further</h2>
  <div class="abs statement-rule"></div>
  <svg class="abs plane-mark" width="22" height="22" viewBox="0 0 22 22" aria-hidden="true"><path d="M2 13 L20 5 L12 20 L10 14 Z" fill="none" stroke="#f2533b" stroke-width="2" stroke-linejoin="round"/></svg>
  <div class="abs label approach-label">Our approach</div>
  <p class="abs approach-text">Lorem ipsum dolor sit amet, consetetur sadipscing elitr, sed diam nonumy eirmod tempor invidunt ut labore et dolore magna aliquyam erat, sed diam voluptua. At vero eos et accusam et justo duo dolores et ea rebum. Stet clita kasd gubergren, no sea takimata sanctus est Lorem ipsum dolor sit amet. Lorem ipsum</p>
</section>

<section>
  <div class="abs cards-rule"></div>
  <article class="abs card" style="left:88px">
    <div class="photo photo-a" role="img" aria-label="Mechanic inspecting a helicopter engine"></div>
    <h3>Aircraft Mechanic</h3>
    <p>Consetetur sadipscing elitr, sed diam nonumy eirmod tempor invidunt ut labore et dolore magna aliquyam erat, sed diam voluptua. At vero eos et accusam et justo duo dolores et ea</p>
    <span class="more">LEARN MORE</span>
  </article>
  <article class="abs card" style="left:440px">
    <div class="photo photo-b" role="img" aria-label="Technician servicing rotor components"></div>
    <h3>Aircraft Mechanic</h3>
    <p>Consetetur sadipscing elitr, sed diam nonumy eirmod tempor invidunt ut labore et dolore magna aliquyam erat, sed diam voluptua. At vero eos et accusam et justo duo dolores et ea</p>
    <span class="more">LEARN MORE</span>
  </article>
  <article class="abs card" style="left:792px">
    <div class="photo photo-c" role="img" aria-label="Crew working inside an aircraft hangar"></div>
    <h3>Aircraft Mechanic</h3>
    <p>Consetetur sadipscing elitr, sed diam nonumy eirmod tempor invidunt ut labore et dolore magna aliquyam erat, sed diam voluptua. At vero eos et accusam et justo duo dolores et ea</p>
    <span class="more">LEARN MORE</span>
  </article>
</section>

<section>
  <div class="abs feature" role="img" aria-label="Mechanic checking landing gear in a bright hangar"></div>
  <div class="abs feature-caption">Join top-tier mechanics across various disciplines</div>
  <div class="abs arrow-btn" style="left:50px"><svg width="14" height="14" viewBox="0 0 14 14"><path d="M9 2 L4 7 L9 12" fill="none" stroke="#fff" stroke-width="2"/></svg></div>
  <div class="abs arrow-btn" style="left:1110px"><svg width="14" height="14" viewBox="0 0 14 14"><path d="M5 2 L10 7 L5 12" fill="none" stroke="#fff" stroke-width="2"/></svg></div>
</section>

<section>
  <h2 class="abs section-title benefits-title">Here to support the<br>whole you</h2>
  <div class="abs label benefits-label">Our benefits</div>
  <div class="abs" style="left:120px;top:3352px">
    <div class="benefit"><svg width="14" height="12" viewBox="0 0 14 12"><path d="M1 6 L5 10 L13 1" fill="none" stroke="#f2533b" stroke-width="2"/></svg>Flexible vacation</div>
    <div class="benefit"><svg width="14" height="12" viewBox="0 0 14 12"><path d="M1 6 L5 10 L13 1" fill="none" stroke="#f2533b" stroke-width="2"/></svg>Family expansion stipend</div>
    <div class="benefit"><svg width="14" height="12" viewBox="0 0 14 12"><path d="M1 6 L5 10 L13 1" fill="none" stroke="#f2533b" stroke-width="2"/></svg>Quarterly offsites &amp; working retreats</div>
    <div class="benefit"><svg width="14" height="12" viewBox="0 0 14 12"><path d="M1 6 L5 10 L13 1" fill="none" stroke="#f2533b" stroke-width="2"/></svg>Weekly demos</div>
  </div>
  <div class="abs" style="left:672px;top:3352px">
    <div class="benefit"><svg width="14" height="12" viewBox="0 0 14 12"><path d="M1 6 L5 10 L13 1" fill="none" stroke="#f2533b" stroke-width="2"/></svg>Monthly social events</div>
    <div class="benefit"><svg width="14" height="12" viewBox="0 0 14 12"><path d="M1 6 L5 10 L13 1" fill="none" stroke="#f2533b" stroke-width="2"/></svg>Monthly wellness stipend</div>
    <div class="benefit"><svg width="14" height="12" viewBox="0 0 14 12"><path d="M1 6 L5 10 L13 1" fill="none" stroke="#f2533b" stroke-width="2"/></svg>Commuter benefits</div>
    <div class="benefit"><svg width="14" height="12" viewBox="0 0 14 12"><path d="M1 6 L5 10 L13 1" fill="none" stroke="#f2533b" stroke-width="2"/></svg>Role growth in SF HQ</div>
  </div>
  <div class="abs divider"></div>
</section>

<section>
  <h2 class="abs section-title roles-title">Come grow<br>with us</h2>
  <div class="abs label roles-label">Our open roles</div>
  <div class="abs" style="left:130px;top:4124px">
    <div class="role"><span class="dot"></span>Position 01</div>
    <div class="role"><span class="dot"></span>Position 01</div>
    <div class="role"><span class="dot"></span>Position 01</div>
  </div>
  <div class="abs" style="left:678px;top:4124px">
    <div class="role"><span class="dot"></span>Position 01</div>
    <div class="role"><span class="dot"></span>Position 01</div>
    <div class="role"><span class="dot"></span>Position 01</div>
  </div>
  <div class="abs btn show-more">SHOW MORE <span>→</span></div>
</section>

<footer class="abs footer"></footer>
<div class="abs footer-rule"></div>
<div class="abs brand foot-brand">KM Aviation</div>
<nav class="abs foot-links">
  <span>Aircraft Maintenance</span><span>About Us</span><span>Careers</span>
  <span>Aircraft Cleaning</span><span>Contact</span><span></span>
</nav>
<div class="abs copyright">© 2024 KM AVIATION. ALL RIGHTS RESERVED.</div>
<div class="abs socials"><span></span><span></span><span></span></div>
<div class="abs btn contact-btn">CONTACT <span>→</span></div>

</body>
</html>
```